Pelin Thai Massage Double Sided Flyer Luxury

I require a double sided flyer
we are a Thai Massage Spa
Would like gold, deep purple and bronze colours
Something eye catching and looks professional

```html
<!DOCTYPE html>
<html lang="en">
<head>
<meta charset="utf-8">
<title>Pelin Thai Massage – Double Sided Flyer</title>
<link href="https://fonts.googleapis.com/css2?family=Libre+Baskerville:wght@400;700&family=Oswald:wght@500;600&family=Roboto:wght@400;500;700&family=Montserrat:wght@500&display=swap" rel="stylesheet">
<style>
  :root {
    --stage: #3a3a3a;
    --brown-deep: #2b190e;
    --brown: #3a2313;
    --gold: #f2b224;
    --gold-soft: #f6c65a;
    --cream: #fff6e4;
    --white: #ffffff;
  }
  * { box-sizing: border-box; margin: 0; padding: 0; }
  html, body { width: 1200px; height: 1200px; overflow: hidden; }
  body { background: var(--stage); position: relative; font-family: "Roboto", sans-serif; }

  .flyer {
    position: absolute; top: 234px; width: 560px; height: 792px;
    transform: scale(0.925); transform-origin: 0 0;
    background: radial-gradient(ellipse at 40% 60%, var(--brown) 0%, var(--brown-deep) 80%);
    overflow: hidden;
    box-shadow: 0 6px 18px rgba(0,0,0,.45);
  }
  .flyer--front { left: 58px; }
  .flyer--back { left: 625px; }

  .photo { position: absolute; }
  .photo--hero-front {
    left: 0; top: 0; width: 560px; height: 380px;
    background: linear-gradient(160deg, #f5ece2 0%, #e8c9a8 40%, #c99a6e 75%, #8d6240 100%);
  }
  .photo--hero-back {
    left: 0; top: 0; width: 560px; height: 300px;
    background: linear-gradient(150deg, #6b4526 0%, #c89070 35%, #e9c7ad 55%, #7b5532 100%);
  }
  .waves { position: absolute; left: 0; top: 0; width: 560px; height: 792px; }

  .bubble {
    position: absolute; border-radius: 50%;
    border: 5px solid var(--gold);
    box-shadow: 0 0 0 2px rgba(255,255,255,.25);
  }

  .brand {
    position: absolute; left: 10px; top: 352px; width: 200px;
    display: flex; flex-direction: column; align-items: center;
  }
  .brand__mark { width: 84px; height: 84px; border-radius: 50%; border: 3px solid var(--gold); }
  .brand__name {
    margin-top: 12px; font-family: "Roboto", sans-serif; font-weight: 400;
    font-size: 19px; color: var(--gold); white-space: nowrap;
  }

  .welcome {
    position: absolute; left: 25px; top: 488px;
    font-family: "Libre Baskerville", serif; font-weight: 700;
    font-size: 29px; line-height: 41px; color: var(--white);
  }
  .intro {
    position: absolute; left: 25px; width: 290px;
    font-size: 10.2px; line-height: 13.8px; color: var(--gold);
  }

  .footer {
    position: absolute; left: 0; bottom: 18px; width: 560px; padding: 0 22px 0 28px;
    display: flex; align-items: flex-end; justify-content: space-between;
    font-family: "Montserrat", sans-serif; font-weight: 500; font-size: 10.5px; color: var(--white);
  }
  .footer__item { display: flex; align-items: flex-end; gap: 5px; }
  .footer__item svg { width: 11px; height: 11px; flex: none; margin-bottom: 1px; }
  .footer__name { color: var(--gold); display: block; }

  .title-serif {
    position: absolute; left: 25px; top: 305px;
    font-family: "Libre Baskerville", serif; font-weight: 700; font-size: 28px; color: var(--gold);
  }
  .tagline { position: absolute; left: 25px; top: 342px; font-size: 10.5px; line-height: 14px; color: var(--white); }
  .title-sans {
    position: absolute; left: 25px; font-family: "Oswald", sans-serif; font-weight: 600;
    color: var(--gold); letter-spacing: .3px;
  }
  .service {
    position: absolute; left: 25px; font-family: "Roboto", sans-serif; font-weight: 500;
    font-size: 15px; color: var(--white); letter-spacing: .3px;
  }
  .price {
    position: absolute; left: 25px; width: 134px; height: 20px;
    display: flex; border: 1.5px solid var(--gold); border-radius: 0 10px 10px 0;
    font-size: 12.5px; font-weight: 500;
  }
  .price__time { background: var(--gold); color: var(--brown-deep); padding: 0 4px; line-height: 17px; width: 74px; }
  .price__cost { color: var(--white); font-weight: 700; font-size: 14px; line-height: 17px; padding-left: 14px; }
  .note { position: absolute; left: 25px; font-size: 10.3px; line-height: 13.8px; color: var(--white); }

  .voucher {
    position: absolute; left: 315px; top: 638px; width: 222px; height: 98px;
    border-radius: 6px;
    background: linear-gradient(135deg, #efe0bd 0%, #d9c08a 60%, #c7a968 100%);
    box-shadow: 0 2px 6px rgba(0,0,0,.5);
    overflow: hidden;
  }
  .voucher__band-h { position: absolute; left: 0; top: 34px; width: 100%; height: 10px; background: #c8161c; }
  .voucher__band-v { position: absolute; left: 44px; top: 0; width: 10px; height: 100%; background: #c8161c; }
  .voucher__title {
    position: absolute; right: 8px; top: 6px;
    font-family: "Oswald", sans-serif; font-weight: 500; font-size: 19px; color: #5a3a1c; letter-spacing: .5px;
  }
  .voucher__sub {
    position: absolute; right: 10px; bottom: 10px;
    font-family: "Libre Baskerville", serif; font-size: 11px; color: #5a3a1c; letter-spacing: 1px;
  }
</style>
</head>
<body>

<section class="flyer flyer--front">
  <div class="photo photo--hero-front" role="img" aria-label="Photo: woman relaxing during a head massage beside a bamboo mat and spa items"></div>
  <svg class="waves" viewBox="0 0 560 792" aria-hidden="true">
    <path d="M0,352 C150,318 300,300 560,335 L560,792 L0,792 Z" fill="var(--brown-deep)"/>
    <path d="M0,352 C150,318 300,300 560,335" fill="none" stroke="var(--gold)" stroke-width="6"/>
    <path d="M0,344 C150,310 300,292 560,327" fill="none" stroke="#fff" stroke-width="1.5" opacity=".8"/>
    <path d="M0,702 Q230,760 560,686" fill="none" stroke="var(--gold)" stroke-width="6"/>
  </svg>

  <div class="bubble" style="left:382px;top:236px;width:216px;height:216px;background:linear-gradient(150deg,#f3e6dd,#d8b8a5 60%,#efe7e2);" role="img" aria-label="Photo: woman receiving a head massage"></div>
  <div class="bubble" style="left:230px;top:330px;width:200px;height:200px;background:linear-gradient(160deg,#9e6a44,#d89a68 50%,#6b4022);" role="img" aria-label="Photo: back massage with candle"></div>
  <div class="bubble" style="left:334px;top:465px;width:242px;height:242px;background:linear-gradient(150deg,#c7b49d,#e8c2a2 45%,#f4eee9);" role="img" aria-label="Photo: woman relaxing during a shoulder massage"></div>

  <div class="brand">
    <span class="brand__mark"></span>
    <span class="brand__name">Pelin Thai Massage</span>
  </div>

  <h1 class="welcome">WELCOME<br>&nbsp;TO LUXURY</h1>

  <p class="intro" style="top:578px;">Set in the heart of Elmwood, Pelin Thai Massage will allow you to immerse yourself in a place where your wellbeing and rejuvenation is at the centre of what we do.</p>
  <p class="intro" style="top:632px;width:274px;">Using Thai traditions, our highly trained therapists offer revitalising body treatments with their deep tissue massage techniques. In their hands, you will see and feel immediate results.</p>

  <footer class="footer">
    <span class="footer__item">
      <svg viewBox="0 0 12 12"><path d="M6 1a3.5 3.5 0 0 0-3.5 3.5C2.5 7 6 10 6 10s3.5-3 3.5-5.5A3.5 3.5 0 0 0 6 1zm0 4.8a1.3 1.3 0 1 1 0-2.6 1.3 1.3 0 0 1 0 2.6z" fill="var(--gold)"/><path d="M1 11.3h10" stroke="var(--gold)" stroke-width="1"/></svg>
      <span><span class="footer__name">Pelin Thai Massage</span>42 Orchard Row Leeds LS7 3QT</span>
    </span>
    <span class="footer__item">
      <svg viewBox="0 0 12 12"><path d="M3 1l2 2.5-1.2 1.2a6 6 0 0 0 3.5 3.5L8.5 7 11 9l-1.3 1.8C5.5 10.5 1.5 6.5 1.2 2.3z" fill="none" stroke="var(--gold)" stroke-width="1.2"/></svg>
      <span>0113 4960218</span>
    </span>
    <span class="footer__item">
      <svg viewBox="0 0 12 12"><circle cx="6" cy="6" r="4.8" fill="none" stroke="var(--gold)" stroke-width="1.1"/><path d="M1.2 6h9.6M6 1.2c-2 2.5-2 7.1 0 9.6M6 1.2c2 2.5 2 7.1 0 9.6" fill="none" stroke="var(--gold)" stroke-width=".9"/></svg>
      <span>www.pelinthaimassage.co.uk</span>
    </span>
  </footer>
</section>

<section class="flyer flyer--back">
  <div class="photo photo--hero-back" role="img" aria-label="Photo: woman in a towel receiving a facial massage with white flowers"></div>
  <svg class="waves" viewBox="0 0 560 792" aria-hidden="true">
    <path d="M0,252 Q160,318 330,262 T560,170 L560,792 L0,792 Z" fill="var(--brown-deep)"/>
    <path d="M0,252 Q160,318 330,262 T560,170" fill="none" stroke="var(--gold)" stroke-width="6"/>
    <path d="M0,244 Q160,310 330,254 T560,162" fill="none" stroke="#fff" stroke-width="1.5" opacity=".8"/>
    <path d="M0,702 Q230,760 560,686" fill="none" stroke="var(--gold)" stroke-width="6"/>
  </svg>

  <div class="bubble" style="left:374px;top:145px;width:200px;height:200px;background:linear-gradient(150deg,#7a4a28,#d7a583 45%,#efe2d8);" role="img" aria-label="Photo: woman with a flower in her hair during a back massage"></div>
  <div class="bubble" style="left:250px;top:214px;width:190px;height:190px;background:linear-gradient(150deg,#4a2b18,#c68a62 50%,#e9d6c8);" role="img" aria-label="Photo: woman relaxing during a back massage"></div>
  <div class="bubble" style="left:330px;top:346px;width:236px;height:236px;background:linear-gradient(150deg,#8a5bb0,#b98a5a 45%,#5a3920);" role="img" aria-label="Photo: spa candle, bath salts and oil bottles"></div>

  <h2 class="title-serif">MASSAGES</h2>
  <p class="tagline">Restore balance. Revive your senses.<br>Discover all the ways Pelin Thai Massage<br>can breathe new life into your body and soul.</p>

  <h2 class="title-sans" style="top:395px;font-size:26px;">MASSAGES</h2>

  <h3 class="service" style="top:434px;">DEEP TISSUE MASSAGE</h3>
  <div class="price" style="top:459px;"><span class="price__time">60 minutes</span><span class="price__cost">£45</span></div>
  <p class="note" style="top:483px;">Oil massage personalised, light to firm pressure</p>
  <div class="price" style="top:508px;"><span class="price__time">90 minutes</span><span class="price__cost">£55</span></div>
  <p class="note" style="top:532px;">Oil massage, medium to firm pressure</p>

  <h3 class="service" style="top:568px;">THAI FLOOR TRADITIONAL MASSAGE</h3>
  <div class="price" style="top:595px;"><span class="price__time">60 minutes</span><span class="price__cost">£45</span></div>
  <p class="note" style="top:619px;">Dry massage, medium to firm pressure<br>applying stretching technique</p>

  <h2 class="title-sans" style="top:662px;font-size:28px;font-weight:500;">OPEN 7 DAYS A WEEK</h2>

  <div class="voucher">
    <span class="voucher__band-h"></span>
    <span class="voucher__band-v"></span>
    <span class="voucher__title">GIFT VOUCHERS</span>
    <span class="voucher__sub">AVAILABLE NOW</span>
  </div>

  <footer class="footer">
    <span class="footer__item">
      <svg viewBox="0 0 12 12"><path d="M6 1a3.5 3.5 0 0 0-3.5 3.5C2.5 7 6 10 6 10s3.5-3 3.5-5.5A3.5 3.5 0 0 0 6 1zm0 4.8a1.3 1.3 0 1 1 0-2.6 1.3 1.3 0 0 1 0 2.6z" fill="var(--gold)"/><path d="M1 11.3h10" stroke="var(--gold)" stroke-width="1"/></svg>
      <span><span class="footer__name">Pelin Thai Massage</span>42 Orchard Row Leeds LS7 3QT</span>
    </span>
    <span class="footer__item">
      <svg viewBox="0 0 12 12"><path d="M3 1l2 2.5-1.2 1.2a6 6 0 0 0 3.5 3.5L8.5 7 11 9l-1.3 1.8C5.5 10.5 1.5 6.5 1.2 2.3z" fill="none" stroke="var(--gold)" stroke-width="1.2"/></svg>
      <span>0113 4960218</span>
    </span>
    <span class="footer__item">
      <svg viewBox="0 0 12 12"><circle cx="6" cy="6" r="4.8" fill="none" stroke="var(--gold)" stroke-width="1.1"/><path d="M1.2 6h9.6M6 1.2c-2 2.5-2 7.1 0 9.6M6 1.2c2 2.5 2 7.1 0 9.6" fill="none" stroke="var(--gold)" stroke-width=".9"/></svg>
      <span>www.pelinthaimassage.co.uk</span>
    </span>
  </footer>
</section>

</body>
</html>
```